Consulting Firm in government policy and finance and in bioethics

I need a logo and a business card for a new consulting company I am creating in NY - I will be consulting on bioethics/government policy. I am looking for a professional appearance to be used on business cards and stationary. - Blue is the preferable color

Industry/Entity Type

Business

Logo Text

The Nerivane Group

```html
<!DOCTYPE html>
<html lang="en">
<head>
<meta charset="utf-8">
<title>The Nerivane Group – Business Card</title>
<link rel="stylesheet" href="https://fonts.googleapis.com/css2?family=Jura:wght@300;400&family=Source+Sans+3:wght@300;400;600&display=swap">
<style>
  :root {
    --page: #ffffff;
    --card: #f2f2f3;
    --card-shadow: #d4d4d5;
    --ink: #7d7d80;
    --ink-soft: #8e8e91;
    --brand-blue: #3a78b8;
  }
  * { margin: 0; padding: 0; box-sizing: border-box; }
  html, body {
    width: 1200px;
    height: 848px;
    overflow: hidden;
    background: var(--page);
  }
  .canvas {
    position: relative;
    width: 1200px;
    height: 848px;
  }
  .card {
    position: absolute;
    left: 222px;
    top: 219px;
    width: 742px;
    height: 396px;
    background: var(--card);
    box-shadow: 5px 6px 0 var(--card-shadow);
    overflow: hidden;
  }
  .brand {
    position: absolute;
    left: 0;
    top: 46px;
    width: 346px;
    display: flex;
    flex-direction: column;
    align-items: center;
  }
  .brand-mark {
    width: 178px;
    height: 178px;
    border-radius: 50%;
    background: var(--brand-blue);
  }
  .brand-name {
    margin-top: 48px;
    font-family: "Jura", sans-serif;
    font-weight: 300;
    font-size: 28px;
    letter-spacing: 1.5px;
    color: var(--ink);
    text-transform: uppercase;
    white-space: nowrap;
    line-height: 1;
  }
  .person {
    position: absolute;
    left: 391px;
    top: 138px;
  }
  .person-name {
    font-family: "Jura", sans-serif;
    font-weight: 300;
    font-size: 35px;
    letter-spacing: 2.5px;
    color: var(--ink);
    text-transform: uppercase;
    line-height: 1;
  }
  .person-role {
    margin-top: 9px;
    margin-left: 8px;
    font-family: "Source Sans 3", sans-serif;
    font-weight: 600;
    font-size: 11px;
    letter-spacing: 3px;
    color: var(--ink-soft);
    text-transform: uppercase;
  }
  .contact {
    position: absolute;
    left: 398px;
    top: 228px;
    list-style: none;
    font-family: "Source Sans 3", sans-serif;
    font-weight: 400;
    font-size: 19px;
    color: var(--ink);
  }
  .contact li {
    display: flex;
    align-items: center;
    height: 26px;
    white-space: nowrap;
  }
  .contact svg {
    width: 14px;
    height: 14px;
    margin-right: 11px;
    flex: none;
    fill: none;
    stroke: var(--ink);
    stroke-width: 1.4;
  }
</style>
</head>
<body>
<main class="canvas">
  <section class="card" aria-label="Business card">
    <div class="brand">
      <div class="brand-mark"></div>
      <div class="brand-name">The Nerivane Group</div>
    </div>

    <div class="person">
      <div class="person-name">Daniel Hale</div>
      <div class="person-role">Manager</div>
    </div>

    <ul class="contact">
      <li>
        <svg viewBox="0 0 14 14" aria-hidden="true"><path d="M7 13 C4 9 3 7 3 5.2 A4 4 0 0 1 11 5.2 C11 7 10 9 7 13 Z"/><circle cx="7" cy="5.2" r="1.3"/></svg>
        New York, 48 Hudson Street,
      </li>
      <li>
        <svg viewBox="0 0 14 14" aria-hidden="true"><rect x="4" y="1" width="6" height="12" rx="1"/><line x1="6" y1="11" x2="8" y2="11"/></svg>
        +1 212 555 0148
      </li>
      <li>
        <svg viewBox="0 0 14 14" aria-hidden="true"><rect x="1.5" y="6" width="11" height="5" rx="1"/><rect x="4" y="2" width="6" height="4"/><line x1="4" y1="9" x2="10" y2="9"/></svg>
        +1 212 555 0149
      </li>
      <li>
        <svg viewBox="0 0 14 14" aria-hidden="true"><circle cx="7" cy="7" r="5.6"/><ellipse cx="7" cy="7" rx="2.4" ry="5.6"/><line x1="1.4" y1="7" x2="12.6" y2="7"/></svg>
        office@nerivanegroup.com
      </li>
      <li>
        <svg viewBox="0 0 14 14" aria-hidden="true"><rect x="1.5" y="3" width="11" height="8"/><polyline points="1.5,3 7,8 12.5,3"/></svg>
        www.nerivanegroup.com
      </li>
    </ul>
  </section>
</main>
</body>
</html>
```